BUSINESS CARD MIRELLE KOSTAVIN

I need a new business card for my personal business.
I am a Naturopath and Nutritionist working doing private consults in the health and wellness arena.
I would like to see designs that are, clean minimalist but colourful.
I like:
White (clean,fresh, minimalist)
pops of one colour ONLY.Choose a colour to run with and keep it simple.
green
light blue
mustard
Bright yellow
Charcoal
The final design should communicate professionalism but also be in touch with nature.
Key Information to include:
MIRELLE KOSTAVIN
ABN 48 207 593 814
MNHAA 682913
Tel 0438 761 942
NATUROPATH | HERBALIST | NUTRITON CONSULTANT
BHSc (Naturopathic Studies) Grad Dip (Naturopathy)
BACK OF CARD : YOUR NEXT APPOINTMENT ..................................
I already have a logo (picture attached)But I would be more than happy to NOT have this included. I am very Open to cards WITHOUT current logo/ ones that weave the colour of my logo but do not use the logo.
I have included pictures attached to give examples of the styles/colors I enjoy.
Updates
I have added a picture of a mortar and pestle - one just like this would be lovely to include in your entry.
TIA

```html
<!DOCTYPE html>
<html lang="en">
<head>
<meta charset="utf-8">
<title>Mirelle Kostavin – Business Card</title>
<link rel="stylesheet" href="https://fonts.googleapis.com/css2?family=Arimo:wght@400;700&display=swap">
<style>
  :root {
    --canvas-bg: #eeeeea;
    --card-white: #ffffff;
    --card-shade: #f1f2ee;
    --leaf-tone: #e6e8e1;
    --lime: #cbdc2a;
    --lime-light: #dde94a;
    --charcoal: #3b3b3b;
    --grey-text: #5f5f5f;
    --band-text: #555a4a;
  }
  * { box-sizing: border-box; margin: 0; padding: 0; }
  html, body { width: 1200px; height: 1000px; overflow: hidden; }
  body {
    background: var(--canvas-bg);
    font-family: "Arimo", Arial, sans-serif;
    position: relative;
  }
  .card {
    position: absolute;
    left: 250px;
    width: 700px;
    height: 400px;
    background: var(--card-white);
    box-shadow: 0 6px 18px rgba(0,0,0,0.12);
    overflow: hidden;
  }
  .card--front { top: 60px; }
  .card--back { top: 540px; }
  .card__texture {
    position: absolute;
    inset: 0;
    background: radial-gradient(ellipse at 30% 40%, var(--card-white) 0%, var(--card-shade) 70%, var(--leaf-tone) 100%);
  }
  .identity {
    position: absolute;
    left: 48px;
    top: 78px;
  }
  .identity__name {
    font-size: 64px;
    font-weight: 400;
    color: var(--charcoal);
    letter-spacing: 1px;
    line-height: 1;
  }
  .identity__roles {
    margin-top: 18px;
    font-size: 17px;
    color: var(--grey-text);
    letter-spacing: 0.6px;
  }
  .identity__qualifications {
    margin-top: 8px;
    font-size: 17px;
    color: var(--grey-text);
  }
  .details-band {
    position: absolute;
    left: 0; right: 0; bottom: 0;
    height: 118px;
    background: linear-gradient(90deg, var(--lime-light), var(--lime));
    display: flex;
    align-items: center;
    justify-content: space-around;
    padding: 0 30px;
  }
  .details-band__item {
    font-size: 17px;
    color: var(--band-text);
    letter-spacing: 0.5px;
  }
  .details-band__divider {
    width: 2px;
    height: 44px;
    background: var(--charcoal);
    transform: rotate(25deg);
  }
  .appointment-band {
    position: absolute;
    left: 0; right: 0;
    top: 140px;
    height: 120px;
    background: linear-gradient(90deg, var(--lime-light), var(--lime));
    display: flex;
    align-items: center;
    padding-left: 48px;
  }
  .appointment-band__label {
    font-size: 30px;
    color: var(--charcoal);
    letter-spacing: 1px;
  }
</style>
</head>
<body>
  <section class="card card--front">
    <div class="card__texture" role="img" aria-label="Faint pale leaf pattern across the white card"></div>
    <div class="identity">
      <h1 class="identity__name">MIRELLE KOSTAVIN</h1>
      <p class="identity__roles">NATUROPATH | HERBALIST | NUTRITON CONSULTANT</p>
      <p class="identity__qualifications">BHSc (Naturopathic Studies) Grad Dip (Naturopathy)</p>
    </div>
    <div class="details-band">
      <span class="details-band__item">ABN 48 207 593 814</span>
      <span class="details-band__divider"></span>
      <span class="details-band__item">QRTWB 682913</span>
      <span class="details-band__divider"></span>
      <span class="details-band__item">Tel 0438 761 942</span>
    </div>
  </section>

  <section class="card card--back">
    <div class="card__texture" role="img" aria-label="Faint pale leaf pattern across the white card"></div>
    <div class="appointment-band">
      <p class="appointment-band__label">YOUR NEXT APPOINTMENT ..........................</p>
    </div>
  </section>
</body>
</html>
```